Design Large Inspirational Artwork with Long Quote

Design a large piece of art with a quote from Marcus Hallwell.

QUOTE
"The thing that's so interesting about being alive is that you're all in. No matter what you do, you're all in. This is gonna kill you, so I think you might as well play the most magnificent game you can while you're waiting. Because, do you have anything better to do? Why not pick the best thing possible that you could do? Because you're more powerful than you think, way more powerful than you think. I mean, God only knows what you are in the final analysis. You're blind to your own weaknesses, but you're also blind to your own strengths. How far could you take that if you stopped wasting time, and if you stopped lying, and if you oriented yourself to the highest possible good that you could conceive of and you committed to that? How much good could you do? Well, I would say: why don't you find out?"

SIZE
A high-resolution print size of 6' wide and 3' tall should provide ample space for both the quote and the accompanying artwork.

TYPOGRAPHY
Choose a bold, clean, and easily readable font for the quote. You could also experiment with different font sizes for certain words or phrases to emphasize their importance within the quote.

COLORS
Since the quote is thought-provoking and reflective, you might want to use a color palette that evokes a sense of introspection and depth. Consider using cool, calming colors like shades of blue, gray, or green. Alternatively, you can use a contrasting color scheme with a light background and dark text to make the quote stand out.

ARTWORK
Select / create / edit background artwork to complement the quote.
While a great design might be minimalistic and/or greyscale, I'd really like to see some full color options. This might be anything from photography or graphics inspired by the ideas in the text, to abstract colors or illustrations that feel like the sentiment expressed.
The art should capture your attention and encourage you to read the text. The art should be visually appealing, both at a distance and up close, regardless of whether the text is read.
Updates

Having trouble confirming the exact print size.

Still looking for printing solution and final size confirmation.

Target Market(s)

Personal, business, office

Industry/Entity Type

None

Font styles to use
Sans Serif
Script

Requirements
Must have
• Entire quote, legible text, modern design, attractive artwork, approx 6ft wide and 3ft tall
Nice to have
• Different font (sizes) for certain words or phrases to emphasize their importance within the quote.

```html
<!DOCTYPE html>
<html lang="en">
<head>
<meta charset="UTF-8">
<title>Why Don't You Find Out — Quote Artwork</title>
<link rel="stylesheet" href="https://fonts.googleapis.com/css2?family=Encode+Sans+Condensed:wght@300&family=Neucha&family=Pinyon+Script&display=swap">
<style>
  :root {
    --violet-bg: #7463ff;
    --violet-bg-light: #8a7cff;
    --violet-deep: #582d98;
    --violet-dusk: #6e4fa8;
    --frame-white: #ffffff;
    --text-soft: #cfc9ff;
    --text-strong: #ffffff;
  }
  html, body {
    margin: 0;
    padding: 0;
    overflow: hidden;
  }
  .artwork {
    position: relative;
    width: 1200px;
    height: 600px;
    overflow: hidden;
    background: linear-gradient(90deg, var(--violet-bg) 0%, var(--violet-bg) 70%, var(--violet-bg-light) 100%);
  }
  .floor-band {
    position: absolute;
    left: 0;
    top: 501px;
    width: 1200px;
    height: 99px;
    background:
      linear-gradient(100deg, rgba(255,255,255,0.55) 0%, rgba(230,215,255,0.35) 25%, rgba(255,255,255,0) 48%),
      linear-gradient(90deg, var(--violet-deep) 0%, var(--violet-deep) 60%, var(--violet-dusk) 100%);
  }
  .doorway-frame {
    position: absolute;
    left: 49px;
    top: 75px;
    width: 200px;
    height: 426px;
    box-sizing: border-box;
    border: 11px solid var(--frame-white);
    border-bottom-width: 10px;
    background: var(--frame-white);
  }
  .doorway-scene {
    display: block;
    width: 100%;
    height: 100%;
  }
  .drop-cap {
    position: absolute;
    left: 291px;
    top: 66px;
    margin: 0;
    font-family: "Pinyon Script", cursive;
    font-size: 92px;
    line-height: 92px;
    color: var(--text-strong);
    text-shadow: 2px 3px 3px rgba(40, 20, 90, 0.6);
  }
  .quote {
    position: absolute;
    left: 303px;
    top: 69px;
    width: 890px;
    margin: 0;
    font-family: "Encode Sans Condensed", "Arial Narrow", sans-serif;
    font-weight: 300;
    font-size: 26px;
    color: var(--text-soft);
  }
  .quote-line {
    display: block;
    white-space: nowrap;
    height: 37px;
    line-height: 37px;
  }
  .quote-line.opening {
    height: 32px;
    line-height: 32px;
    padding-left: 69px;
  }
  .emphasis {
    font-family: "Neucha", cursive;
    font-size: 30px;
    color: var(--text-strong);
  }
  .closing-line {
    position: absolute;
    left: 303px;
    top: 437px;
    margin: 0;
    white-space: nowrap;
    font-family: "Neucha", cursive;
    font-size: 41px;
    line-height: 50px;
    color: var(--text-strong);
  }
</style>
</head>
<body>
<main class="artwork">
  <div class="floor-band"></div>

  <div class="doorway-frame">
    <svg class="doorway-scene" viewBox="0 0 178 405" preserveAspectRatio="none" role="img" aria-label="Illustration of two figures standing in a glowing open doorway">
      <defs>
        <linearGradient id="doorway-glow" x1="0" y1="0" x2="0" y2="1">
          <stop offset="0" stop-color="#5a2e96"/>
          <stop offset="0.6" stop-color="#7a64d8"/>
          <stop offset="0.78" stop-color="#b2a8ff"/>
          <stop offset="1" stop-color="#2a2238"/>
        </linearGradient>
      </defs>
      <rect width="178" height="405" fill="url(#doorway-glow)"/>
    </svg>
  </div>

  <span class="drop-cap" aria-hidden="true">T</span>
  <p class="quote" aria-label="The thing that’s so interesting about being alive is that you’re all in.">
    <span class="quote-line opening">he thing that’s so interesting about being alive is that you’re all in. No matter</span>
    <span class="quote-line opening">what you do, you’re all in. This is gonna kill you, so I think you might as well</span>
    <span class="quote-line">play the most magnificent game you can while you’re waiting. <span class="emphasis">Because, do you</span></span>
    <span class="quote-line"><span class="emphasis">have anything better to do? Why not pick the best thing possible that you</span></span>
    <span class="quote-line"><span class="emphasis">could do?</span> Because you’re more powerful than you think, way more powerful than</span>
    <span class="quote-line">you think. I mean, <span class="emphasis">God</span> only knows what you are in the final analysis. You’re blind to</span>
    <span class="quote-line">your own weaknesses, but you’re also blind to your own strengths. <span class="emphasis">How far could</span></span>
    <span class="quote-line"><span class="emphasis">you take that if you stopped wasting time, and if you stopped lying, and if</span></span>
    <span class="quote-line"><span class="emphasis">you oriented yourself to the highest possible good that you could conceive</span></span>
    <span class="quote-line"><span class="emphasis">of and you committed to that? How much good could you do?</span></span>
  </p>

  <p class="closing-line">Well, I would say: why don’t you find out?</p>
</main>
</body>
</html>
```